Legal Journal cover - modern and sylish

We require a cover design for a new, modern and digital legal academic journal. Attached is our logo so you can get an idea of the feel. This academic journal will have several editions per year.Requirements for the cover design:-The feel of the cover is to be modern -In harmony with our logo-While staying uniform and set in its design,
Updates

Colors
ec1f27

Requirements
Must have
• 1) Colour. Each edition will use different colours. (So we will need the source files to be able to continue to do this)
• 2) An image section. We would like to be able to put in different image or photo with each edition. So we need to have a section, most likely in the shape of a strip, that can include a different image or photo each edition. This part is where we can put a different image in for each edition. So this section would need to be able to accommodate different types of images. It could be a single square. Or it could be a line (a strip) that an image or images.
• 3) A title for the edition and volume and number. Like this:
• Volume 34, No 2 (2016): Contemporary Issues in Criminal Law
• I have attached a range of journals I found online to serve as inspiration.

```html
<!DOCTYPE html>
<html lang="en">
<head>
<meta charset="utf-8">
<title>Volume 34, No 2 (2016): Contemporary Issues in Criminal Law</title>
<link rel="stylesheet" href="https://fonts.googleapis.com/css2?family=Roboto:wght@300;400;500;700&display=swap">
<style>
  :root {
    --paper: #ffffff;
    --volume-numeral: #bdbdbd;
    --volume-label: #9d9d9d;
    --issue-number: #c6c6c6;
    --title-ink: #6b6b6b;
    --accent: #ec1f27;
    --accent-veil: rgba(236, 31, 39, 0.82);
    --photo-dark: #050505;
    --photo-sky: #3d67c9;
    --photo-light: #cfe0f2;
  }
  * { margin: 0; padding: 0; box-sizing: border-box; }
  html, body {
    width: 849px;
    height: 1200px;
    overflow: hidden;
    background: var(--paper);
  }
  .cover {
    position: relative;
    width: 849px;
    height: 1200px;
    background: var(--paper);
    font-family: "Roboto", Arial, sans-serif;
    overflow: hidden;
  }
  .volume-label {
    position: absolute;
    left: 29px;
    top: 22px;
    font-size: 26px;
    font-weight: 700;
    letter-spacing: -0.5px;
    color: var(--volume-label);
  }
  .volume-numeral {
    position: absolute;
    left: 18px;
    top: 20px;
    font-size: 322px;
    line-height: 1;
    font-weight: 500;
    letter-spacing: -14px;
    color: var(--volume-numeral);
  }
  .publisher {
    position: absolute;
    right: 51px;
    top: 205px;
    display: flex;
    align-items: center;
    gap: 12px;
  }
  .publisher-dot {
    width: 36px;
    height: 36px;
    border-radius: 50%;
    background: var(--accent);
  }
  .publisher-name {
    font-size: 27px;
    font-weight: 500;
    letter-spacing: 0.5px;
    color: var(--accent);
  }
  .issue-heading {
    position: absolute;
    left: 100px;
    right: 53px;
    top: 360px;
    display: flex;
    align-items: baseline;
    justify-content: space-between;
    white-space: nowrap;
  }
  .issue-number {
    font-size: 36px;
    font-weight: 500;
    color: var(--issue-number);
  }
  .issue-title {
    font-size: 34px;
    font-weight: 700;
    letter-spacing: -0.3px;
    color: var(--title-ink);
  }
  .title-rule {
    position: absolute;
    left: 204px;
    top: 406px;
    width: 590px;
    height: 1.5px;
    background: var(--accent);
  }
  .issue-year {
    position: absolute;
    right: 53px;
    top: 414px;
    font-size: 38px;
    font-weight: 300;
    color: var(--title-ink);
  }
  .feature-image {
    position: absolute;
    left: 0;
    top: 533px;
    width: 849px;
    height: 667px;
    background:
      linear-gradient(150deg, transparent 55%, rgba(207,224,242,0.85) 70%, transparent 82%),
      linear-gradient(115deg, var(--photo-sky) 0%, #5f86d6 10%, var(--photo-light) 18%, var(--photo-dark) 28%, var(--photo-dark) 62%, #8fb4e6 74%, var(--photo-dark) 86%, var(--photo-dark) 100%);
  }
  .accent-panel {
    position: absolute;
    left: 382px;
    top: 533px;
    width: 415px;
    height: 324px;
    background: var(--accent-veil);
    mix-blend-mode: multiply;
  }
</style>
</head>
<body>
  <main class="cover">
    <div class="volume-label">VOLUME</div>
    <div class="volume-numeral">34</div>

    <div class="publisher">
      <span class="publisher-dot"></span>
      <span class="publisher-name">LEX MERIDIAN</span>
    </div>

    <h1 class="issue-heading">
      <span class="issue-number">No 2</span>
      <span class="issue-title">Contemporary Issues in Criminal Law</span>
    </h1>
    <div class="title-rule"></div>
    <div class="issue-year">2016</div>

    <div class="feature-image" role="img" aria-label="Edition photograph: abstract reflections of blue sky and clouds in angled black glass panels"></div>
    <div class="accent-panel"></div>
  </main>
</body>
</html>
```